Website for a company offering full serivce charging solutions for electric cars

The company "vorn-werk" (english: "front-works") offering all-in-one-solutions for charging infrastructure for electric mobility.

There are four products:
1- Wallboxes for single-family homes
2- Solutions for property devloper/-management for property parking space
3- All-in-one-charging solution for municipalities/communities
4- Solutions for tourism/hotels/holiday appartments

The Website structure:
1. Main Page
2.1. Product Page Single Homes
2.2. Product Page Property Management / Parking
2.3. Product Page Municipality
2.4. Product Page Tourism
3. Contact Form / Request for information
4. Imprint / Legal

The Website should be built on Wordpress with a powerful possibility to simply add/modify specific landing pages.

We would like you to implement the website later and also maintain it if possible, but we would be able to do minor modifications by ourselfs (for A/B-Testing)

The website should be clear and simple, easy to understand.
Target group is mainly B2C without deeper knowledge of that topic.

It should suggest, that we will provide a very simple way to get the charging infrastructure done.

We need a contact form, maybe we will use Leadmill later.

Attached you will find a draft of the main page and a landing page (for 2.2) - it is just the content, please ignore the design. We would love to let you create a suitable design.
Also you will find some drafts a bit different for the same story.

I added also a few stock photos, but they don't need to be used! If you have better ideas, you are welcome!

Charging/Electric mobility

Sans Serif

• Based on Wordpress, and the designer should be able to implement it on Wordpress on a later step

```html
<!DOCTYPE html>
<html lang="de">
<head>
<meta charset="utf-8">
<title>vorn-werk.de – Website Design</title>
<link rel="stylesheet" href="https://fonts.googleapis.com/css2?family=Lexend+Exa:wght@500;600&family=Poppins:wght@400;500;600;700&display=swap">
<style>
:root{
  --board:#222838;
  --dark:#1b1f2e;
  --magenta:#e4129c;
  --purple:#8b50d6;
  --ink:#1d2030;
  --grey:#6b6f7c;
  --light:#f3f3f6;
  --white:#ffffff;
  --grad:linear-gradient(90deg,var(--magenta),var(--purple));
}
*{box-sizing:border-box;margin:0;padding:0}
html,body{width:1200px;height:2861px;overflow:hidden;background:var(--board)}
body{position:relative;font-family:"Poppins",sans-serif;color:var(--ink)}
.board-title{position:absolute;left:0;width:1200px;top:286px;text-align:center;font-weight:500;font-size:64px;letter-spacing:1px;color:var(--white)}
.page{position:absolute;width:418px;background:var(--white);overflow:hidden}
.page-home{left:157px;top:453px;height:1483px}
.page-business{left:157px;top:1936px;height:753px}
.page-private{left:626px;top:453px;height:966px}
.page-municipal{left:626px;top:1463px;height:828px}
.abs{position:absolute}
.block{position:absolute}
.site-nav{position:absolute;left:30px;right:30px;top:10px;height:14px;display:flex;align-items:center;justify-content:space-between;z-index:5}
.brand{font-weight:500;font-size:9px;color:var(--ink)}
.on-dark .brand{color:var(--white)}
.site-nav nav{display:flex;align-items:center;gap:10px;font-size:4.6px;font-weight:500}
.site-nav a{color:var(--ink);text-decoration:none}
.on-dark .site-nav a{color:var(--white)}
.site-nav a.active{color:var(--magenta)!important}
.btn-contact{border:1px solid var(--magenta);border-radius:8px;padding:2px 8px;font-weight:700;font-size:4.2px}
.section-title{font-family:"Lexend Exa",sans-serif;font-weight:600;font-size:11px;line-height:11.5px;letter-spacing:-.3px;color:var(--ink);margin-bottom:4px}
.light{color:var(--white)!important}
.text{font-size:4.4px;line-height:6.6px;color:var(--grey)}
.text p+p{margin-top:3px}
.text b{color:var(--ink)}
.on-grad .text,.on-grad .text b{color:var(--white)}
.text+.ticks,.ticks+.text,.sub-lead+.ticks{margin-top:3px}
ul.ticks{list-style:none;font-size:4.4px;line-height:6.2px;color:var(--grey)}
ul.ticks li{position:relative;padding-left:7px;margin-bottom:1.2px}
ul.ticks li::before{content:"";position:absolute;left:0;top:1.2px;width:4px;height:4px;border-radius:50%;background:var(--magenta)}
.on-grad ul.ticks li{color:var(--white)}
.on-grad ul.ticks li::before{background:var(--white)}
ul.ticks li.sub{padding-left:14px}
ul.ticks li.sub::before{left:8px;width:2px;height:2px;top:2.2px}
.photo{position:absolute;overflow:hidden}
.round{border-radius:50%}
.rounded{border-radius:8px}
.pill{display:inline-block;margin-top:8px;border-radius:10px;font-size:4.2px;font-weight:700;padding:4px 10px;text-transform:uppercase;letter-spacing:.2px}
.pill-white{background:var(--white);color:var(--magenta)}
.pill-grad{background:var(--grad);color:var(--white)}
.link-more{display:inline-block;margin-top:6px;font-size:4.6px;font-weight:600;color:var(--magenta);text-decoration:underline}
.site-footer{position:absolute;left:0;right:0;bottom:0;height:183px}
.site-footer svg.wave{position:absolute;left:0;top:0;width:418px;height:183px}
.footer-brand{position:absolute;top:92px;left:0;right:0;text-align:center;font-weight:500;font-size:11px;color:var(--white)}
.footer-links{position:absolute;top:116px;left:0;right:0;display:flex;justify-content:center;gap:8px;font-size:4.6px;color:var(--white)}
.footer-social{position:absolute;top:133px;left:0;right:0;display:flex;justify-content:center;gap:6px}
.footer-social span{width:11px;height:11px;border-radius:50%;border:1px solid rgba(255,255,255,.35);display:block;position:relative}
.footer-social span::after{content:"";position:absolute;left:3.5px;top:3.5px;width:2px;height:2px;border-radius:50%;background:var(--white)}
.footer-rule{position:absolute;top:159px;left:0;right:0;height:1px;background:rgba(255,255,255,.12)}
.footer-copy{position:absolute;top:168px;left:0;right:0;text-align:center;font-size:4.2px;color:var(--white)}
.to-top{position:absolute;top:157px;right:14px;width:10px;height:10px;border-radius:50%;background:var(--magenta)}
.hero-kicker{position:absolute;top:73px;left:0;right:0;text-align:center;font-family:"Lexend Exa",sans-serif;font-size:7.5px;font-weight:500;color:var(--white)}
.hero-title{position:absolute;top:85px;left:0;right:0;text-align:center;font-weight:500;font-size:25px;color:var(--white)}
.hero-sub{position:absolute;top:116px;left:0;right:0;text-align:center;font-size:4.4px;color:rgba(255,255,255,.8)}
.sub-lead{font-size:4.8px;line-height:6.4px;font-weight:700;margin-bottom:3px}
.center{text-align:center}
</style>
</head>
<body>

<div class="board-title">vorn-werk.de</div>

<!-- Home page -->
<section class="page page-home on-dark">
  <svg class="abs" style="left:0;top:0" width="418" height="1483" viewBox="0 0 418 1483" aria-hidden="true">
    <defs>
      <linearGradient id="homeGrad" x1="0" y1="0" x2="1" y2="0">
        <stop offset="0" stop-color="#e4129c"/><stop offset="1" stop-color="#8b50d6"/>
      </linearGradient>
    </defs>
    <path d="M0 250 H418 V545 C380 600 300 605 210 575 C130 548 60 528 0 535 Z" fill="url(#homeGrad)"/>
    <path d="M0 0 H418 V262 C360 300 290 340 200 338 C110 336 40 310 0 300 Z" fill="#1b1f2e"/>
    <path d="M0 880 C90 835 200 832 300 862 C360 880 400 872 418 864 V1092 C300 1120 150 1065 0 1085 Z" fill="#f3f3f6"/>
  </svg>

  <header class="site-nav">
    <span class="brand">vorn-werk.de</span>
    <nav><a class="active">Lösungen</a><a>Unternehmen</a><a>Services</a><a>Karriere</a><a class="btn-contact">KONTAKT</a></nav>
  </header>

  <div class="hero-kicker">Willkommen bei</div>
  <div class="hero-title">vorn-werk</div>
  <div class="hero-sub">All-in-One-Lösungen für Ladeinfrastruktur für Elektromobilität anzubieten.</div>
  <div class="photo rounded" role="img" aria-label="Illustration: Ladesäule und violettes Elektroauto an einer geschwungenen Straße" style="left:70px;top:132px;width:330px;height:150px;background:linear-gradient(135deg,#2a2f45,#6a3fa8 60%,#b03bc4)"></div>

  <div class="on-grad">
    <div class="photo round" role="img" aria-label="Foto: leuchtender Ladestecker an einem Elektroauto" style="left:-20px;top:383px;width:202px;height:184px;background:radial-gradient(circle at 55% 45%,#3fd0f5,#123a5c 55%,#0d1624)"></div>
    <div class="block" style="left:207px;top:398px;width:192px">
      <h2 class="section-title light">vorn-werk ist Ihr Partner</h2>
      <div class="sub-lead light">wenn das Laden nicht nur einfach, sondern die Umsetzung auch aus einer Hand kommen soll</div>
      <div class="text">
        <p>Wir bieten Lösungen sowohl für <b>Privatkunden, Geschäftskunden</b> als auch <b>Kommunen</b> an, die schnell, fair und ohne Eigenleistung zu einer smarten Ladelösung für E-Fahrzeuge kommen möchten.</p>
        <p>Von der Beratung über die Installation, Inbetriebnahme bis zur Abrechnung und Wartung bekommen Sie bei vorn-werk alles aus einer Hand. Auf Wunsch vermieten wir auch die Ladetechnik und übernehmen im gewerblichen Bereich die direkte Abrechnung mit dem Nutzer. Für Kommunen bieten wir den kostenlosen Full-Service an und beteiligen die Gemeinden an der Nutzung der Infrastruktur.</p>
        <p>Fragen Sie uns nach der auf Ihre individuellen Bedürfnisse zugeschnittenen Lösung.</p>
      </div>
    </div>
  </div>

  <div class="block" style="left:30px;top:655px;width:190px">
    <h2 class="section-title">als Privatkunde</h2>
    <ul class="ticks">
      <li>Bestandsanalyse mit umfangreicher Beratung über die Möglichkeiten der Umsetzung</li>
      <li>Prüfung und Übernahme der Anmeldung verfügbarer Fördermöglichkeiten</li>
      <li>Auswahl an smarten Wallbox Lösungen, passend für Ihr Fahrzeug und Ihre Bedürfnisse</li>
      <li>Installation inkl. aller notwendigen Materialien und Tätigkeiten (Durchbrüche, Erdarbeiten, etc.)</li>
      <li>Inbetriebnahme und Einweisung in die Ladetechnik</li>
      <li>Jährlich technische Wartung nach Vorgabe</li>
      <li>Reparaturservice, unter Berücksichtigung der geltenden Garantie Ansprüche</li>
    </ul>
  </div>
  <div class="photo" role="img" aria-label="Foto: Mann im weißen Pullover hält ein Ladekabel vor blauem Himmel" style="left:230px;top:613px;width:156px;height:184px;background:linear-gradient(160deg,#6fa6e0,#cfe1f4 55%,#9aa4b4);border-radius:4px"></div>

  <div class="photo round" role="img" aria-label="Foto: Mann lädt ein weißes Elektroauto an einer Ladestation" style="left:32px;top:899px;width:164px;height:164px;background:radial-gradient(circle at 40% 40%,#eef0f3,#b7bcc6 60%,#6d7380)"></div>
  <div class="block" style="left:207px;top:908px;width:192px">
    <h2 class="section-title">als Geschäftskunde</h2>
    <ul class="ticks">
      <li>Durchführung einer individuellen Bedarfsanalyse inkl. Ermittlung der Anforderungen für:</li>
      <li class="sub">Haus- und Immobilienverwaltungen</li>
      <li class="sub">Dienstleistungs- und Handelsunternehmen</li>
      <li class="sub">Hotel und Beherbergungsbetriebe</li>
      <li class="sub">Parkraum- und Parkhausbetreiber</li>
      <li class="sub">Tourismus, Sport- und Freizeiteinrichtungen</li>
      <li>Planung und Projektierung des Installationsaufwands inkl. Materialverbrauch</li>
      <li>Leasing oder Kauf der Hardware</li>
      <li>Normgerechte Installation der Ladeinfrastruktur inkl. Durchbrüche, Brandschutz- und Erdarbeiten</li>
      <li>Bei Bestandsbauten Integration der Ladeinfrastruktur in die Gebäudesystemtechnik und ggf. Anpassung des Netzanschlusses</li>
    </ul>
    <a class="link-more">Weiterlesen</a>
  </div>

  <div class="block" style="left:30px;top:1155px;width:200px">
    <h2 class="section-title">als Kommune</h2>
    <ul class="ticks">
      <li>Konzeptionierung möglicher Ladeinfrastrukturen innerhalb Ihrer Gemeinde</li>
      <li>Planung und Projektsteuerung inkl. sämtlicher behördlicher Genehmigungsverfahren und Beantragung von Fördermitteln</li>
      <li>Fachgerechte Installation und Inbetriebnahme</li>
      <li>Regelmäßige Wartung gemäß Vorschrift</li>
      <li>Reparatur und Kundenservice</li>
      <li>Direkte Abrechnung mit dem Nutzer</li>
      <li>Beteiligung der Gemeinde am Umsatz</li>
      <li>Möglichkeit der Integration von Bonusprogrammen, mit denen der lokale Einzelhandel beworben wird</li>
    </ul>
  </div>
  <div class="photo" role="img" aria-label="Foto: weiße Wallbox mit schwarzem aufgerolltem Ladekabel" style="left:249px;top:1141px;width:111px;height:172px;background:linear-gradient(180deg,#f1f2f4,#d9dce1 45%,#2a2d35);border-radius:30px 30px 50% 50%"></div>

  <footer class="site-footer">
    <svg class="wave" viewBox="0 0 418 183" preserveAspectRatio="none" aria-hidden="true">
      <defs><linearGradient id="fw1" x1="0" y1="0" x2="1" y2="0"><stop offset="0" stop-color="#e4129c"/><stop offset="1" stop-color="#8b50d6"/></linearGradient></defs>
      <path d="M0 62 C60 30 120 10 190 18 C270 28 360 60 418 0 V183 H0 Z" fill="url(#fw1)"/>
      <path d="M0 70 C60 40 120 20 190 26 C270 34 360 66 418 8 V183 H0 Z" fill="#1b1f2e"/>
    </svg>
    <div class="footer-brand">vorn-werk.de</div>
    <div class="footer-links"><span>AGB</span><span>Datenschutzerklärung</span><span>Impressum</span><span>Kontakt</span><span>Karriere</span><span>FAQs</span></div>
    <div class="footer-social"><span></span><span></span><span></span></div>
    <div class="footer-rule"></div>
    <div class="footer-copy">©vorn-werk GmbH</div>
    <div class="to-top"></div>
  </footer>
</section>

<!-- Business page -->
<section class="page page-business">
  <svg class="abs" style="left:0;top:0" width="418" height="753" viewBox="0 0 418 753" aria-hidden="true">
    <defs><linearGradient id="blush" x1="0" y1="0" x2="0" y2="1"><stop offset="0" stop-color="#fbf1f9"/><stop offset="1" stop-color="#f6ecf7"/></linearGradient></defs>
    <path d="M0 250 C90 225 160 228 240 248 C320 268 380 262 418 250 V600 H0 Z" fill="url(#blush)"/>
  </svg>
  <header class="site-nav">
    <span class="brand">vorn-werk.de</span>
    <nav><a class="active">Lösungen</a><a>Unternehmen</a><a>Services</a><a>Karriere</a><a class="btn-contact">KONTAKT</a></nav>
  </header>

  <div class="block" style="left:30px;top:84px;width:198px">
    <h2 class="section-title">Bieten Sie Ihren Mietern, Mitarbeitern, Kunden, Gästen noch mehr Komfort</h2>
    <div class="text">
      <p>Wir beraten, planen und setzen um, die Lösung die Ihr Unternehmen, Wohnpark, Tourismuseinrichtung noch attraktiver macht</p>
      <p>Ob Kaufen oder Mieten, wir haben DIE Lösung für SIE!</p>
      <p>vorn-werk richtet sich mit seinem Angebot für Gewerbebetriebe speziell an:</p>
    </div>
    <ul class="ticks">
      <li>Haus- und Immobilienverwaltungen</li>
      <li>Dienstleistungs- und Handelsunternehmen</li>
      <li>Hotel und Beherbergungsbetriebe</li>
      <li>Parkraum- und Parkhausbetreiber</li>
      <li>Tourismus, Sport- und Freizeiteinrichtungen</li>
    </ul>
  </div>
  <div class="photo rounded" role="img" aria-label="Foto: Nahaufnahme einer Ladebuchse am Fahrzeug" style="left:236px;top:44px;width:151px;height:162px;background:radial-gradient(circle at 50% 50%,#a0a6b2,#3b404b 55%,#15181f)"></div>

  <div class="photo rounded" role="img" aria-label="Foto: Hand steckt einen Ladestecker in ein silbernes Elektroauto" style="left:30px;top:303px;width:155px;height:233px;background:linear-gradient(150deg,#d5d9df,#8b929d 55%,#3d434d)"></div>
  <div class="block" style="left:210px;top:322px;width:190px">
    <h2 class="section-title">Laden als Service Dienstleistung</h2>
    <div class="text">Wenn Sie keine zusätzlichen Kosten und Aufwand mit der Errichtung von Ladepunkten möchten, dann ist unser Modell „Laden als Service Dienstleistung“ genau das richtige für Sie.</div>
    <ul class="ticks">
      <li>Wir prüfen die örtlichen Gegebenheiten und erstellen eine Machbarkeitsstudie, die wir auf Wunsch auch vor Ihren Eigentümern, Unternehmen oder Geschäftsführung vorstellen.</li>
      <li>Wir übernehmen die notwendigen Genehmigungsverfahren und suchen nach den geeigneten Fördermöglichkeiten</li>
      <li>Wir bieten Ihnen eine Auswahl an smarten Normal- oder Schnellademöglichkeiten</li>
      <li>Wir koordinieren die Planung mit allen Gewerken und kümmern uns um die fach- und normgerechte Installation</li>
      <li>Wir stellen die Inbetriebnahme sicher und integrieren die Lösung in Ihre bestehende Infrastruktur, bzw. richten für Mieter, Mitarbeiter, Kunden entsprechende Nutzerkonten ein</li>
      <li>Wir unterstützen Sie bei der Lade-Abrechnung ODER übernehmen diese direkt mit Ihren Nutzern</li>
      <li>Wir sorgen uns um die notwendige Wartung und stehen Ihnen für Reparaturen jederzeit zur Verfügung</li>
      <li>Wir helfen Ihren Nutzern wenn es einmal nicht so funktioniert wie wir es uns wünschen</li>
    </ul>
  </div>

  <footer class="site-footer">
    <svg class="wave" viewBox="0 0 418 183" preserveAspectRatio="none" aria-hidden="true">
      <defs><linearGradient id="fw2" x1="0" y1="0" x2="1" y2="0"><stop offset="0" stop-color="#e4129c"/><stop offset="1" stop-color="#8b50d6"/></linearGradient></defs>
      <rect width="418" height="70" fill="#f6ecf7"/>
      <path d="M0 62 C60 30 120 10 190 18 C270 28 360 60 418 0 V183 H0 Z" fill="url(#fw2)"/>
      <path d="M0 70 C60 40 120 20 190 26 C270 34 360 66 418 8 V183 H0 Z" fill="#1b1f2e"/>
    </svg>
    <div class="footer-brand">vorn-werk.de</div>
    <div class="footer-links"><span>AGB</span><span>Datenschutzerklärung</span><span>Impressum</span><span>Kontakt</span><span>Karriere</span><span>FAQs</span></div>
    <div class="footer-social"><span></span><span></span><span></span></div>
    <div class="footer-rule"></div>
    <div class="footer-copy">©vorn-werk GmbH</div>
    <div class="to-top"></div>
  </footer>
</section>

<!-- Private customer page -->
<section class="page page-private">
  <svg class="abs" style="left:0;top:0" width="418" height="966" viewBox="0 0 418 966" aria-hidden="true">
    <defs><linearGradient id="privGrad" x1="0" y1="0" x2="1" y2="0"><stop offset="0" stop-color="#e4129c"/><stop offset="1" stop-color="#8b50d6"/></linearGradient></defs>
    <path d="M0 320 C60 300 110 330 150 380 C200 420 300 420 380 390 C400 384 412 380 418 378 V560 C400 580 380 600 330 615 C250 630 120 635 0 640 Z" fill="url(#privGrad)"/>
  </svg>
  <header class="site-nav">
    <span class="brand">vorn-werk.de</span>
    <nav><a class="active">Lösungen</a><a>Unternehmen</a><a>Services</a><a>Karriere</a><a class="btn-contact">KONTAKT</a></nav>
  </header>

  <div class="block" style="left:30px;top:92px;width:192px">
    <h2 class="section-title">Schnell und einfach zu Ihrer privaten Wallbox</h2>
    <div class="text">
      <p>Von der Bestandsaufnahme, über die Beratung möglicher Lösungen, bis zur Installation und Inbetriebnahme alles aus EINER Hand.</p>
      <p>Und wenn Sie wünschen, dann leihen wir Ihnen die Wallbox auch gerne gegen eine kleine Nutzungspauschale.</p>
    </div>
  </div>
  <div class="photo" role="img" aria-label="Illustration: pinkes Elektroauto an einer Ladesäule vor Windrädern" style="left:213px;top:41px;width:178px;height:150px;background:linear-gradient(135deg,#f2f2f5,#e8c8e8 50%,#c74fc7 75%,#7d4fd0);border-radius:10px"></div>

  <div class="photo round" role="img" aria-label="Foto: Ladestecker in der Ladebuchse eines Autos" style="left:30px;top:206px;width:167px;height:165px;background:radial-gradient(circle at 45% 45%,#e8eaee,#9aa1ac 55%,#3f4450);border:3px solid #fff"></div>
  <div class="block" style="left:209px;top:234px;width:190px">
    <h2 class="section-title">Eine Wallbox nach Ihren Wünschen</h2>
    <div class="text">Wir finden gemeinsam die beste Lösung für Sie. Egal,</div>
    <ul class="ticks">
      <li>welches E-Mobil Sie betanken möchten</li>
      <li>welche Länge Ihr Anschlusskabel an Ihr Fahrzeug besitzen soll</li>
      <li>ob Sie einen eigenen Stromzähler mit besonders günstigem Strom anbinden möchten</li>
      <li>Sie eine bestehende Photovoltaikanlage integrieren möchten</li>
      <li>Sie eine monatliche Übersicht Ihrer „getankten“ kWh haben möchten</li>
      <li>Sie zwecks der Abrechnung mit Ihrem Arbeitgeber oder als Selbstständiger verschiedene E-PKWs oder Ladevorgänge voneinander trennen wollen</li>
    </ul>
  </div>

  <div class="block on-grad" style="left:30px;top:480px;width:192px">
    <h2 class="section-title light">Schlüsselfertig alles aus einer Hand</h2>
    <div class="sub-lead light">Sie haben einen Ansprechpartner der für Sie</div>
    <ul class="ticks">
      <li>die Erstberatung übernimmt</li>
      <li>die Fördermöglichkeiten eruiert und ggf. beantragt</li>
      <li>die Installation mit allen benötigten Gewerken fachgerecht, sauber und schnell koordiniert</li>
      <li>die Inbetriebnahme und Einweisung sicherstellt</li>
      <li>die notwendige jährliche Wartung im Auge behält und organisiert</li>
      <li>bei Problemen oder Störungen zur Seite steht</li>
    </ul>
    <span class="pill pill-white">Jetzt Angebot anfordern</span>
  </div>
  <div class="photo" role="img" aria-label="Foto: lächelnde Frau mit Smartphone hält ein Ladekabel" style="left:230px;top:456px;width:155px;height:183px;background:linear-gradient(160deg,#dfe3ea,#b9c1cc 50%,#5d6878);border-radius:4px"></div>

  <div class="block center" style="left:80px;top:710px;width:258px">
    <h2 class="section-title">Auf Wunsch auch geliehen</h2>
    <div class="text">Sie scheuen die hohen Investitionskosten? Dann bieten wir Ihnen eine Lösung bei der Sie Ihre Wallbox von uns mieten können. Selbst die Installation von bis zu 25 Meter Anschlusslänge bis zum nächsten Stromzähler und bei Objekten im Raum Oberbayern kostet Sie nichts, wenn Sie mit uns einen 24 Monats Mietvertrag über 50€ / Monat abschließen.</div>
  </div>

  <footer class="site-footer">
    <svg class="wave" viewBox="0 0 418 183" preserveAspectRatio="none" aria-hidden="true">
      <defs><linearGradient id="fw3" x1="0" y1="0" x2="1" y2="0"><stop offset="0" stop-color="#e4129c"/><stop offset="1" stop-color="#8b50d6"/></linearGradient></defs>
      <path d="M0 62 C60 30 120 10 190 18 C270 28 360 60 418 0 V183 H0 Z" fill="url(#fw3)"/>
      <path d="M0 70 C60 40 120 20 190 26 C270 34 360 66 418 8 V183 H0 Z" fill="#1b1f2e"/>
    </svg>
    <div class="footer-brand">vorn-werk.de</div>
    <div class="footer-links"><span>AGB</span><span>Datenschutzerklärung</span><span>Impressum</span><span>Kontakt</span><span>Karriere</span><span>FAQs</span></div>
    <div class="footer-social"><span></span><span></span><span></span></div>
    <div class="footer-rule"></div>
    <div class="footer-copy">©vorn-werk GmbH</div>
    <div class="to-top"></div>
  </footer>
</section>

<!-- Municipality page -->
<section class="page page-municipal">
  <svg class="abs" style="left:0;top:0" width="418" height="828" viewBox="0 0 418 828" aria-hidden="true">
    <defs><linearGradient id="blush2" x1="0" y1="0" x2="0" y2="1"><stop offset="0" stop-color="#fbf1f9"/><stop offset="1" stop-color="#f4eaf7"/></linearGradient></defs>
    <path d="M0 430 C90 400 170 395 250 415 C330 435 380 430 418 420 V700 H0 Z" fill="url(#blush2)"/>
  </svg>
  <header class="site-nav">
    <span class="brand">vorn-werk.de</span>
    <nav><a class="active">Lösungen</a><a>Unternehmen</a><a>Services</a><a>Karriere</a><a class="btn-contact">KONTAKT</a></nav>
  </header>

  <div class="block" style="left:30px;top:70px;width:210px">
    <h2 class="section-title">Wir bringen Ihre Gemeinde mit klimafördernden Maßnahmen in die Schlagzeilen</h2>
    <div class="text">
      <p>Ohne entsprechende Lade-Infrastruktur für E-Autos für Bürger aber auch Besucher der Gemeinde wird E-Mobilität nicht den notwendigen Drive erfahren.</p>
      <p>Kümmern uns darum, dass Ihre Ladesäulen gefunden werden, und tragen Sie in den gängigen Ladenetzportalen ein.</p>
      <p>Nicht jeder Bürger hat die Möglichkeit sich eine Lademöglichkeit zu Hause aufzubauen. Besucher aus der Umgebung sind dankbar und suchen nach Lademöglichkeiten in Ihrem Ausflugsziel, aufgrund mangelnder Lademöglichkeiten in der Stadt.</p>
    </div>
  </div>
  <div class="photo round" role="img" aria-label="Illustration: violettes Elektroauto zwischen Ladestecker, Tropfen und Zapfpistole" style="left:252px;top:53px;width:150px;height:150px;background:radial-gradient(circle at 50% 50%,#c15ed2,#7a4fd0 40%,#2b2f42 70%,#ffffff 71%)"></div>

  <div class="photo" role="img" aria-label="Foto: Hand hält einen Ladestecker an einem Auto" style="left:30px;top:220px;width:159px;height:170px;background:linear-gradient(150deg,#c9ced6,#7e8692 55%,#3a3f4a);box-shadow:7px 7px 0 #8b50d6"></div>
  <div class="block" style="left:209px;top:256px;width:192px">
    <h2 class="section-title">Wir übernehmen die Koordination und Finanzierung und lassen Sie dennoch mit verdienen</h2>
    <div class="text">
      <p>Unser Angebot ist es Ihnen der Gemeinde die notwendige Infrastruktur zu finanzieren, den Aufbau zu organisieren, und den 24/7 Betrieb sicherzustellen.</p>
      <p>Neben der Unterstützung der lokalen Infrastruktur sollen sie als Gemeinde auch an den Erlösen der Ladevorgänge beteiligt sein.</p>
    </div>
  </div>

  <div class="block" style="left:30px;top:485px;width:178px">
    <h2 class="section-title">Wir rechnen mit dem Kunden direkt ab</h2>
    <div class="text">
      <p>Gleichgültig wie der Kunde seinen Ladevorgang bezahlen möchte, wir bieten ihm die einfachste Lösung.</p>
      <p>Angeschlossen an die üblichen Roamingpartner kann der Kunde mit seiner bestehenden Ladekarte (Fahrclub Nord, Stromwerk Süd etc.) zahlen, oder aber auch direkt per Kreditkarte, Bezahldienst oder weiteren Zahlungsmöglichkeiten.</p>
      <p>Wir rechnen den Kunden exakt nach seinem bezogenen Stromverbrauch ab. Keine unfaire Pauschal- oder Standzeitabrechnung. Wir rechnen frühestens nach 3-5 Stunden eine Branchen übliche Belegungsgebühr erheben, sollte der Ladevorgang bereits abgeschlossen sein.</p>
    </div>
  </div>
  <div class="block" style="left:217px;top:485px;width:182px">
    <h2 class="section-title">Wir verstehen die Kommunen als unsere Partner</h2>
    <div class="text">
      <p>Trotzdem, dass wir die Kosten für Infrastruktur und Installation übernehmen, den Betrieb sicherstellen, und den Kunden ein einwandfreies Ladeerlebnis garantieren, beteiligen wir Sie als unseren Partner am Erfolg.</p>
      <p>Neben der anteiligen Umsatzbeteiligung bieten wir die Möglichkeit der Integration des lokalen Einzelhandels über ein Bonusprogramm. Ebenso besteht die Möglichkeit Ihre bereits vorhandene Parkraumbewirtschaftung in unser Konzept zu integrieren.</p>
    </div>
    <span class="pill pill-grad">Sprechen Sie jetzt mit uns</span>
  </div>

  <footer class="site-footer">
    <svg class="wave" viewBox="0 0 418 183" preserveAspectRatio="none" aria-hidden="true">
      <defs><linearGradient id="fw4" x1="0" y1="0" x2="1" y2="0"><stop offset="0" stop-color="#e4129c"/><stop offset="1" stop-color="#8b50d6"/></linearGradient></defs>
      <rect width="418" height="70" fill="#f4eaf7"/>
      <path d="M0 62 C60 30 120 10 190 18 C270 28 360 60 418 0 V183 H0 Z" fill="url(#fw4)"/>
      <path d="M0 70 C60 40 120 20 190 26 C270 34 360 66 418 8 V183 H0 Z" fill="#1b1f2e"/>
    </svg>
    <div class="footer-brand">vorn-werk.de</div>
    <div class="footer-links"><span>AGB</span><span>Datenschutzerklärung</span><span>Impressum</span><span>Kontakt</span><span>Karriere</span><span>FAQs</span></div>
    <div class="footer-social"><span></span><span></span><span></span></div>
    <div class="footer-rule"></div>
    <div class="footer-copy">©vorn-werk GmbH</div>
    <div class="to-top"></div>
  </footer>
</section>

</body>
</html>
```